K7T Business Cards

I need a very sleek design using the logo attached. I want something very simple and clean, yet still creative. On the black I would like some sort of matte black finish, so make the design that will fit that accordingly.

I have attached the information needed in the card with the logo image.

Business

```html
<!DOCTYPE html>
<html lang="en">
<head>
<meta charset="utf-8">
<title>K7T Business Cards</title>
<link href="https://fonts.googleapis.com/css2?family=Montserrat:wght@700;800&family=Open+Sans:wght@400;600&display=swap" rel="stylesheet">
<style>
  :root {
    --backdrop: #e4e4e4;
    --card-black: #0c0c0c;
    --card-white: #ffffff;
    --brand-blue: #2a73d9;
    --accent-orange: #f07a1a;
    --ink: #1a1a1a;
    --ink-soft: #8a8a8a;
    --ink-faint: #4a4a4a;
  }
  * { margin: 0; padding: 0; box-sizing: border-box; }
  html, body { width: 1200px; height: 750px; overflow: hidden; }
  body {
    background: var(--backdrop);
    position: relative;
    font-family: "Open Sans", sans-serif;
  }
  .card {
    position: absolute;
    width: 525px;
    height: 300px;
    border-radius: 4px;
    box-shadow: 0 14px 30px rgba(0,0,0,0.22);
  }
  .card--front {
    left: 70px;
    top: 380px;
    background: var(--card-black);
  }
  .card--back {
    left: 605px;
    top: 70px;
    background: var(--card-white);
  }
  .front-mark {
    position: absolute;
    left: 0; right: 0;
    top: 108px;
    text-align: center;
    font-family: "Montserrat", sans-serif;
    font-weight: 800;
    font-size: 64px;
    letter-spacing: 2px;
    color: var(--brand-blue);
  }
  .front-web {
    position: absolute;
    left: 0; right: 0;
    bottom: 40px;
    text-align: center;
    font-size: 10px;
    letter-spacing: 5px;
    color: var(--ink-faint);
  }
  .back-brand {
    position: absolute;
    left: 38px;
    top: 44px;
    display: flex;
    align-items: center;
    gap: 8px;
    font-family: "Montserrat", sans-serif;
    font-weight: 800;
    font-size: 26px;
    color: var(--brand-blue);
  }
  .brand-dot {
    width: 10px; height: 10px;
    border-radius: 50%;
    background: var(--accent-orange);
  }
  .contact {
    position: absolute;
    right: 40px;
    top: 136px;
    text-align: right;
  }
  .contact__name {
    font-family: "Montserrat", sans-serif;
    font-weight: 700;
    font-size: 22px;
    color: var(--ink);
  }
  .contact__role {
    font-size: 12px;
    color: var(--ink-soft);
    margin-bottom: 6px;
  }
  .contact__line {
    font-size: 12px;
    line-height: 19px;
    color: var(--ink-soft);
  }
  .contact__line::after {
    content: "";
    display: inline-block;
    width: 6px; height: 6px;
    margin-left: 8px;
    border-radius: 50%;
    background: var(--accent-orange);
    vertical-align: middle;
  }
</style>
</head>
<body>
  <section class="card card--back">
    <div class="back-brand"><span>K7T Kestrel</span><span class="brand-dot"></span></div>
    <div class="contact">
      <p class="contact__name">Owen Hartley</p>
      <p class="contact__role">Sales Executive</p>
      <p class="contact__line">289.555.0147</p>
      <p class="contact__line">hello@k7t.net</p>
      <p class="contact__line">www.k7t.net</p>
    </div>
  </section>

  <section class="card card--front">
    <div class="front-mark">K7T</div>
    <p class="front-web">www.k7t.net</p>
  </section>
</body>
</html>
```